Business Cards Design for the electrical wholesaler: clean bold dynamic :)

We need a business card design that would follow our latest brand guidelines. As an electrical wholesaler we want to bring a fresh look and feel into the industry. The design should be clean bold and dynamic. It should come alive with the renewed energy of our green colour. Our grey colour should keep things balanced and complement the notion of maturity and responsibility. We employ Lato as a corporate font however are not bound by this font and we’re open to interpretation here.

Target Market(s)

Electrical contractors

Industry/Entity Type

Business

Contact Information for Business Card

Logo
Name & Surname: Olesia Hrybenko
Job Title: Director of Marketing
Email: olesia.hrybenko@mailvex.com
Cell phone: XXX.XXX.XXXX
Address: 20517 - 88 Ave. Edmonton, AB, Canada. T6K 2N8
Business Phone: 780.362.7048
Website: www.kopra.ca

Font styles to use
Other font styles liked:
• Lato

Requirements
Must have
• Logo & website
Nice to have
• Brand elements - some of them you may find in the attached Brand Guidelines (e.g. three lines on the background signifying "W")

```html
<!DOCTYPE html>
<html lang="en">
<head>
<meta charset="utf-8">
<title>Kopra Business Card</title>
<link href="https://fonts.googleapis.com/css2?family=Lato:wght@400;700&family=Arimo:wght@400&display=swap" rel="stylesheet">
<style>
  :root {
    --page-bg: #e4e3e0;
    --card-bg: #f6f6f4;
    --brand-green: #6aac3c;
    --brand-green-band: #5f9f32;
    --brand-grey: #3f3f41;
    --text-grey: #525254;
    --rule-grey: #7a7a7c;
    --band-dark: #333334;
    --web-text: #e9f3e1;
  }
  html, body {
    margin: 0;
    padding: 0;
    width: 1200px;
    height: 970px;
    overflow: hidden;
    background: var(--page-bg);
  }
  .business-card {
    position: absolute;
    left: 80px;
    top: 197px;
    width: 1040px;
    height: 575px;
    background: var(--card-bg);
    border-radius: 18px;
    box-shadow: 0 2px 10px rgba(0,0,0,0.12);
    overflow: hidden;
    font-family: 'Lato', sans-serif;
  }
  .brand {
    position: absolute;
    left: 52px;
    top: 62px;
    display: flex;
    align-items: center;
    gap: 18px;
  }
  .brand-square {
    width: 62px;
    height: 62px;
    background: var(--brand-green);
  }
  .brand-name {
    font-family: 'Lato', sans-serif;
    font-weight: 400;
    font-size: 96px;
    line-height: 1;
    color: var(--brand-grey);
    letter-spacing: -1px;
  }
  .person-name {
    position: absolute;
    left: 51px;
    top: 222px;
    margin: 0;
    font-weight: 700;
    font-size: 42px;
    color: var(--brand-green);
  }
  .person-title {
    position: absolute;
    left: 52px;
    top: 275px;
    margin: 0;
    font-weight: 400;
    font-size: 27px;
    color: var(--text-grey);
  }
  .divider {
    position: absolute;
    left: 51px;
    top: 350px;
    width: 931px;
    height: 2px;
    background: var(--rule-grey);
  }
  .contact-list {
    position: absolute;
    left: 51px;
    top: 370px;
    margin: 0;
    padding: 0;
    list-style: none;
    font-family: 'Arimo', sans-serif;
    font-size: 23px;
    color: var(--text-grey);
  }
  .contact-list li {
    display: flex;
    align-items: center;
    height: 34.5px;
  }
  .contact-icon {
    width: 22px;
    height: 22px;
    margin-right: 12px;
    fill: var(--brand-green);
  }
  .address {
    position: absolute;
    right: 58px;
    top: 402px;
    margin: 0;
    text-align: right;
    font-family: 'Arimo', sans-serif;
    font-style: normal;
    font-size: 23px;
    line-height: 34.5px;
    color: #2e2e30;
  }
  .footer-band {
    position: absolute;
    left: 0;
    top: 500px;
    width: 1040px;
    height: 40px;
  }
  .website {
    position: absolute;
    left: 676px;
    top: 500px;
    width: 270px;
    height: 40px;
    line-height: 40px;
    text-align: center;
    font-family: 'Lato', sans-serif;
    font-size: 22px;
    letter-spacing: 3px;
    color: var(--web-text);
  }
</style>
</head>
<body>
  <div class="business-card">
    <div class="brand">
      <div class="brand-square"></div>
      <span class="brand-name">kopra</span>
    </div>

    <h1 class="person-name">Olesia Hrybenko</h1>
    <p class="person-title">Director of Marketing</p>

    <div class="divider"></div>

    <ul class="contact-list">
      <li>
        <svg class="contact-icon" viewBox="0 0 24 24" aria-hidden="true">
          <path d="M7 1h10a2 2 0 0 1 2 2v18a2 2 0 0 1-2 2H7a2 2 0 0 1-2-2V3a2 2 0 0 1 2-2zm0 3v14h10V4H7zm5 15.2a1.2 1.2 0 1 0 0 2.4 1.2 1.2 0 0 0 0-2.4z"/>
        </svg>
        780.362.7048
      </li>
      <li>
        <svg class="contact-icon" viewBox="0 0 24 24" aria-hidden="true">
          <path d="M6.6 10.8a15.1 15.1 0 0 0 6.6 6.6l2.2-2.2a1 1 0 0 1 1-.25 11.4 11.4 0 0 0 3.6.57 1 1 0 0 1 1 1V20a1 1 0 0 1-1 1A17 17 0 0 1 3 4a1 1 0 0 1 1-1h3.5a1 1 0 0 1 1 1c0 1.25.2 2.45.57 3.6a1 1 0 0 1-.25 1z"/>
        </svg>
        780.362.7048
      </li>
      <li>
        <svg class="contact-icon" viewBox="0 0 24 24" aria-hidden="true">
          <path d="M2 5h20v14H2V5zm2 2v.5l8 5 8-5V7H4zm0 2.8V17h16V9.8l-8 5-8-5z"/>
        </svg>
        olesia.hrybenko@mailvex.com
      </li>
    </ul>

    <address class="address">
      20517 - 88 Ave. Edmonton<br>
      AB, Canada. T6K 2N8
    </address>

    <svg class="footer-band" viewBox="0 0 1040 40" aria-hidden="true">
      <polygon points="0,0 650,0 666,40 0,40" fill="var(--band-dark)"/>
      <polygon points="660,0 944,0 960,40 676,40" fill="var(--brand-green-band)"/>
      <polygon points="956,0 1040,0 1040,40 972,40" fill="var(--band-dark)"/>
    </svg>
    <span class="website">www.kopra.ca</span>
  </div>
</body>
</html>
```